Advertisement Sign

Hello,
We're in need of a new design for an advertisement sign. Below is our current concept, but we're looking for improvements. Specifically, we'd like to enhance the size of the 'Call for Assistance' text, possibly explore different fonts, and possibly add a background to make the design more engaging and less plain. We need something that sticks out more. Any suggestions are welcome.

Target Market(s)

Construction and Landscape Companies

```html
<!DOCTYPE html>
<html lang="en">
<head>
<meta charset="UTF-8">
<title>Ridgeline Rentals – Call for Assistance Sign</title>
<link href="https://fonts.googleapis.com/css2?family=Montserrat:wght@600;800&family=Oswald:wght@600&display=swap" rel="stylesheet">
<style>
  :root {
    --page: #e4e6e9;
    --sign-white: #f2f2f2;
    --brand-blue: #2a78c0;
    --ink: #1f1f1f;
    --tag-grey: #6e6e6e;
    --text-light: #f4f4f4;
  }
  * { margin: 0; padding: 0; box-sizing: border-box; }
  html, body {
    width: 1200px;
    height: 800px;
    overflow: hidden;
    background: var(--page);
  }
  .sign {
    position: absolute;
    left: 40px;
    top: 120px;
    width: 1120px;
    height: 560px;
    background: var(--sign-white);
    overflow: hidden;
  }
  .sign__band {
    position: absolute;
    left: 0;
    right: 0;
    top: 346px;
    bottom: 0;
    background: var(--brand-blue);
  }
  .brand {
    position: absolute;
    left: 100px;
    top: 92px;
    width: 920px;
    display: flex;
    align-items: center;
    gap: 28px;
  }
  .brand__mark {
    width: 84px;
    height: 84px;
    background: var(--brand-blue);
    flex: none;
  }
  .brand__name {
    font-family: "Montserrat", sans-serif;
    font-weight: 800;
    font-size: 68px;
    letter-spacing: 1px;
    color: var(--ink);
    white-space: nowrap;
    line-height: 1;
  }
  .tagline {
    position: absolute;
    left: 340px;
    top: 228px;
    width: 700px;
    display: flex;
    align-items: center;
    gap: 28px;
  }
  .tagline__rule {
    flex: 1;
    height: 3px;
    background: var(--tag-grey);
  }
  .tagline__text {
    font-family: "Montserrat", sans-serif;
    font-weight: 600;
    font-size: 19px;
    letter-spacing: 3.5px;
    color: var(--tag-grey);
    white-space: nowrap;
  }
  .cta {
    position: absolute;
    left: 90px;
    top: 283px;
    width: 940px;
    height: 126px;
    background: var(--ink);
    border: 4px solid var(--sign-white);
    border-radius: 63px;
    display: flex;
    align-items: center;
    justify-content: center;
  }
  .cta__text {
    font-family: "Oswald", sans-serif;
    font-weight: 600;
    font-size: 100px;
    line-height: 1;
    color: var(--text-light);
    letter-spacing: 1px;
    margin-top: -4px;
  }
  .contact {
    position: absolute;
    left: 116px;
    top: 432px;
    display: flex;
    align-items: center;
    gap: 20px;
  }
  .contact__icon {
    width: 96px;
    height: 96px;
    flex: none;
  }
  .contact__number {
    font-family: "Montserrat", sans-serif;
    font-weight: 800;
    font-size: 106px;
    letter-spacing: -3px;
    line-height: 1;
    color: var(--text-light);
  }
</style>
</head>
<body>
  <main class="sign">
    <div class="sign__band"></div>

    <div class="brand">
      <div class="brand__mark"></div>
      <span class="brand__name">RIDGELINE RENTALS</span>
    </div>

    <div class="tagline">
      <span class="tagline__rule"></span>
      <span class="tagline__text">BUILT TO KEEP YOU MOVING</span>
      <span class="tagline__rule"></span>
    </div>

    <div class="cta">
      <span class="cta__text">CALL FOR ASSISTANCE</span>
    </div>

    <div class="contact">
      <svg class="contact__icon" viewBox="0 0 100 100" aria-hidden="true">
        <circle cx="50" cy="50" r="50" fill="#f4f4f4"/>
        <path d="M32 27 l8 -3 l8 13 l-6 5 c3 7 8 12 15 15 l5 -6 l13 8 l-3 8 c-2 4 -7 5 -11 4 c-15 -5 -27 -17 -32 -32 c-1 -4 0 -9 3 -12 z"
              fill="none" stroke="#2a78c0" stroke-width="3" stroke-linejoin="round"/>
        <path d="M56 33 a12 12 0 0 1 11 11" fill="none" stroke="#2a78c0" stroke-width="3" stroke-linecap="round"/>
        <path d="M57 24 a21 21 0 0 1 19 19" fill="none" stroke="#2a78c0" stroke-width="3" stroke-linecap="round"/>
      </svg>
      <span class="contact__number">403-555-0184</span>
    </div>
  </main>
</body>
</html>
```